Law firm for traffic law - company portfolio

Company folder with logo and picture on the front. On the back only the imprint in DinA4 format. The following folders are ordered
https://www.papierhof-lenzbach.de/mappe-fuer-din-a4-2teilig-mit-2-laschen-40-farbig-aussseite-bedruck-mit-mattfolie-kaschiert.html#content-view

```html
<!DOCTYPE html>
<html lang="de">
<head>
<meta charset="utf-8">
<title>LEXMOBIL – Mappe</title>
<link rel="stylesheet" href="https://fonts.googleapis.com/css2?family=Jost:wght@400;500;600;700&display=swap">
<style>
  :root{
    --navy:#033a5c;
    --orange:#f39c13;
    --white:#ffffff;
    --ink:#1f2a33;
    --cut:#e8559a;
    --fold:#39a9d6;
  }
  *{margin:0;padding:0;box-sizing:border-box}
  html,body{width:1200px;height:883px;overflow:hidden;background:var(--white)}
  body{font-family:"Jost",sans-serif}
  .sheet{position:absolute;left:0;top:0;width:1372px;height:1012px;transform:scale(0.8746,0.8725);transform-origin:0 0}
  .artwork{position:absolute;left:0;top:0;width:1372px;height:1012px}
  .brand{position:absolute;top:48px;font-weight:600;font-size:32px;letter-spacing:3px;color:var(--navy);line-height:1}
  .brand--back{left:200px}
  .brand--front{left:1140px}
  .section-title{position:absolute;font-weight:600;font-size:21px;letter-spacing:.5px;color:var(--navy)}
  .contacts-title{left:316px;top:196px}
  .team{position:absolute;top:246px;width:210px}
  .team--left{left:249px}
  .team--right{left:476px;width:240px}
  .person{margin-bottom:14px;font-size:11px;line-height:14.5px;color:var(--ink)}
  .person__name{font-weight:600;font-size:12px;color:var(--navy)}
  .imprint-title{left:506px;top:668px}
  .imprint{position:absolute;left:475px;top:717px;font-size:11.5px;line-height:15.5px;color:var(--navy);font-weight:500}
  .imprint__row{display:flex;gap:10px;align-items:center}
  .imprint__item{display:flex;align-items:center;gap:4px}
  .imprint__item svg{width:12px;height:12px;fill:var(--navy)}
  .imprint__gap{height:12px}
  .headline{position:absolute;left:835px;top:660px;font-weight:700;font-size:31px;line-height:35px;letter-spacing:.8px;color:var(--navy)}
  .subline{position:absolute;left:835px;top:744px;font-weight:400;font-size:22px;line-height:27px;letter-spacing:.5px;color:var(--navy)}
</style>
</head>
<body>
<div class="sheet">
  <svg class="artwork" viewBox="0 0 1372 1012" xmlns="http://www.w3.org/2000/svg">
    <defs>
      <linearGradient id="photoTone" x1="0" y1="0" x2="1" y2="1">
        <stop offset="0" stop-color="#9aa49a"/>
        <stop offset=".35" stop-color="#c9a23a"/>
        <stop offset=".6" stop-color="#6f7f91"/>
        <stop offset="1" stop-color="#9b9a98"/>
      </linearGradient>
    </defs>
    <g fill="none" stroke="var(--cut)" stroke-width="1" stroke-dasharray="4 3">
      <path d="M153,0 L30,30 Q5,40 5,70 L5,800 Q5,820 30,825 L153,856"/>
      <path d="M153,856 L190,900 Q170,930 180,960 Q200,1000 260,990 L300,1010"/>
      <path d="M762,856 L740,1000 L712,1010"/>
      <path d="M762,0 L1372,0"/>
      <path d="M1372,160 L1372,190"/>
      <path d="M762,856 L1372,856"/>
    </g>
    <path d="M36,730 L36,745 L105,812 L120,812" fill="none" stroke="var(--cut)" stroke-width="1"/>
    <path d="M548,878 A14,14 0 0 0 576,878" fill="none" stroke="var(--cut)" stroke-width="1"/>
    <path d="M702,928 A14,14 0 0 0 702,956" fill="none" stroke="var(--cut)" stroke-width="1"/>

    <rect x="153" y="0" width="609" height="856" fill="var(--white)"/>
    <path d="M153,160 L730,40 Q755,34 762,0 L762,44 L195,184 Q160,193 153,212 Z" fill="var(--navy)"/>

    <path d="M762,44 L1372,190 L1372,670 L762,560 Z" fill="url(#photoTone)" role="img" aria-label="Foto: Mann im Anzug sitzt erschöpft an einem verunfallten gelben Auto"/>
    <path d="M762,0 Q768,36 800,44 L1372,160 L1372,190 Q1350,166 1320,160 L800,60 Q770,56 762,44 Z" fill="var(--navy)"/>

    <path d="M153,660 L735,548 Q758,542 762,520 Q766,542 790,548 L1372,660 L1372,887 L762,887 L762,856 L153,856 Z" fill="var(--navy)"/>
    <path d="M175,856 L175,712 Q178,690 205,684 L762,578 L762,856 Z" fill="var(--orange)"/>
    <path d="M762,578 L1310,680 Q1348,688 1350,725 L1350,887 L762,887 Z" fill="var(--orange)"/>
    <line x1="762" y1="0" x2="762" y2="856" stroke="var(--fold)" stroke-width=".8"/>

    <rect x="250" y="705" width="158" height="88" rx="6" fill="var(--navy)" opacity=".18" role="img" aria-label="Illustration: zwei zusammengestoßene Autos"/>
  </svg>

  <div class="brand brand--back">LEXMOBIL</div>
  <div class="brand brand--front">LEXMOBIL</div>

  <h2 class="section-title contacts-title">IHRES ANSPRECHPARTNER</h2>

  <div class="team team--left">
    <div class="person"><div class="person__name">TOBIAS BRENNEKE</div>Rechtsanwalt<br>Fachanwalt für Verkehrsrecht<br>brenneke@lexmobil.de</div>
    <div class="person"><div class="person__name">HEIKE HASSELT</div>Rechtsanwältin<br>hasselt@lexmobil.de</div>
    <div class="person"><div class="person__name">STEFAN DORNFELD</div>Rechtsanwalt<br>dornfeld@lexmobil.de</div>
    <div class="person"><div class="person__name">KATRIN LESSNER</div>Rechtsanwältin<br>lessner@lexmobil.de</div>
    <div class="person"><div class="person__name">ANJA MARWEDE</div>Rechtsanwältin<br>Leiterin Zweigstelle Lindenbrück<br>marwede@lexmobil.de</div>
  </div>

  <div class="team team--right">
    <div class="person"><div class="person__name">FLORIAN KROLL</div>Rechtsanwalt<br>Fachanwalt für Verkehrsrecht<br>kroll@lexmobil.de</div>
    <div class="person"><div class="person__name">MATTHIAS HARTING, LL.M.</div>Rechtsanwalt<br>Fachanwalt für Verkehrsrecht<br>harting@lexmobil.de</div>
    <div class="person"><div class="person__name">CLAUDIA BERG-OSTERKAMP</div>Rechtsanwältin<br>Fachanwältin für Verkehrsrecht<br>berg-osterkamp@lexmobil.de</div>
    <div class="person"><div class="person__name">UWE TIEMEYER</div>Rechtsanwalt<br>Fachanwalt für Verkehrsrecht<br>tiemeyer@lexmobil.de</div>
  </div>

  <h2 class="section-title imprint-title">KONTAKTDATEN</h2>
  <div class="imprint">
    <div>LEXMOBIL GbR- Kanzlei für Verkehrsrecht</div>
    <div>Lindenring 14, 30159 Hannover</div>
    <div class="imprint__gap"></div>
    <div class="imprint__row">
      <span class="imprint__item"><svg viewBox="0 0 24 24"><path d="M6.6 10.8a15 15 0 0 0 6.6 6.6l2.2-2.2c.3-.3.7-.4 1-.2 1.1.4 2.3.6 3.6.6.6 0 1 .4 1 1V20c0 .6-.4 1-1 1A17 17 0 0 1 3 4c0-.6.4-1 1-1h3.5c.6 0 1 .4 1 1 0 1.3.2 2.5.6 3.6.1.3 0 .7-.2 1z"/></svg>0511 9 38 21 40</span>
      <span class="imprint__item"><svg viewBox="0 0 24 24"><path d="M6 2h10v6H6zM3 9h18v10h-3v3H6v-3H3zm5 7v4h8v-4z"/></svg>0511 9 38 21 41</span>
    </div>
    <div class="imprint__row">
      <span class="imprint__item"><svg viewBox="0 0 24 24"><path d="M2 5h20v14H2zm2 2v1l8 5 8-5V7l-8 5z"/></svg>info@lexmobil.de</span>
      <span class="imprint__item"><svg viewBox="0 0 24 24"><path d="M12 2a10 10 0 1 0 0 20 10 10 0 0 0 0-20zm0 2c1 1.2 1.8 3 2 5h-4c.2-2 1-3.8 2-5zM4.3 11h3.8c.1 1.5.4 2.9 1 4.2A8 8 0 0 1 4.3 11zm3.8-2H4.3a8 8 0 0 1 4.8-4.2c-.6 1.3-.9 2.7-1 4.2zm2 2h3.8c-.2 2-1 3.8-1.9 5-1-1.2-1.7-3-1.9-5zm5.8 0h3.8a8 8 0 0 1-4.8 4.2c.6-1.3.9-2.7 1-4.2zm0-2c-.1-1.5-.4-2.9-1-4.2A8 8 0 0 1 19.7 9z"/></svg>www.LEXMOBIL.de</span>
    </div>
  </div>

  <h1 class="headline">PROFESSIONELLES<br>UNFALL-MANAGEMENT</h1>
  <p class="subline">DIE KOMPETENTE ABWICKLUNG<br>IHRES VERKEHRSUNFALLES</p>
</div>
</body>
</html>
```